Accounting firm needing business card / letterhead designed
Marcus T. Elbering, CPA
marcus@fernquill.com
www.fernquill.com
482 N Harlow Ave Halverton, OH 43719
272-555-0172

```html
<!DOCTYPE html>
<html lang="en">
<head>
<meta charset="utf-8">
<title>Fernquill – Business Card</title>
<link rel="stylesheet" href="https://fonts.googleapis.com/css2?family=Ubuntu:wght@300;400;500;700&display=swap">
<style>
  :root {
    --navy: #252a5e;
    --lime: #82cd2a;
    --paper: #ffffff;
    --edge: #d6d6d6;
    --canvas: #ffffff;
  }
  * { margin: 0; padding: 0; box-sizing: border-box; }
  html, body {
    width: 1005px;
    height: 1200px;
    overflow: hidden;
    background: var(--canvas);
    font-family: "Ubuntu", Arial, sans-serif;
  }
  .canvas { position: relative; width: 1005px; height: 1200px; }
  .card {
    position: absolute;
    left: 25px;
    width: 955px;
    height: 550px;
    background: var(--paper);
    border: 1px solid var(--edge);
    overflow: hidden;
  }
  .card--front { top: 30px; }
  .card--back { top: 606px; }
  .card__shapes {
    position: absolute;
    inset: 0;
    width: 100%;
    height: 100%;
  }
  .fill-navy { fill: var(--navy); }
  .fill-lime { fill: var(--lime); }

  /* Front */
  .brand {
    position: absolute;
    left: 0;
    right: 0;
    top: 172px;
    text-align: center;
    color: var(--navy);
    font-weight: 700;
    font-size: 110px;
    letter-spacing: 2px;
    line-height: 1;
  }
  .website {
    position: absolute;
    left: 0;
    right: 0;
    top: 360px;
    text-align: center;
    color: var(--navy);
    font-size: 20px;
    font-weight: 400;
  }

  /* Back */
  .person {
    position: absolute;
    left: 0;
    right: 0;
    top: 164px;
    text-align: center;
    color: var(--navy);
    font-size: 50px;
    line-height: 1;
  }
  .person__name { font-weight: 700; }
  .person__title { font-weight: 400; }
  .contact {
    position: absolute;
    left: 292px;
    top: 240px;
    list-style: none;
    color: var(--paper);
    font-size: 25px;
    font-weight: 300;
    line-height: 37px;
  }
  .contact__item { display: flex; align-items: flex-start; }
  .contact__icon {
    width: 22px;
    height: 22px;
    margin-top: 8px;
    margin-right: 4px;
    flex: none;
    fill: none;
    stroke: var(--paper);
    stroke-width: 1.4;
  }
  .contact__icon--solid { fill: var(--paper); stroke: none; }
</style>
</head>
<body>
<main class="canvas">

  <section class="card card--front" aria-label="Card front">
    <svg class="card__shapes" viewBox="0 0 836 477" preserveAspectRatio="none" aria-hidden="true">
      <polygon class="fill-lime" points="0,0 160,0 160,110 0,199"/>
      <rect class="fill-navy" x="160" y="0" width="258" height="110"/>
      <rect class="fill-lime" x="418" y="0" width="258" height="110"/>
      <polygon class="fill-navy" points="676,0 836,0 676,110"/>
      <polygon class="fill-navy" points="160,370 160,477 0,477"/>
      <rect class="fill-lime" x="160" y="370" width="258" height="107"/>
      <rect class="fill-navy" x="418" y="370" width="258" height="107"/>
      <polygon class="fill-lime" points="836,282 836,477 676,477 676,370"/>
    </svg>
    <h1 class="brand">Fernquill</h1>
    <p class="website">www.fernquill.com</p>
  </section>

  <section class="card card--back" aria-label="Card back">
    <svg class="card__shapes" viewBox="0 0 836 477" preserveAspectRatio="none" aria-hidden="true">
      <polygon class="fill-lime" points="0,197 160,110 676,110 836,0 836,283 676,370 160,370 0,477"/>
    </svg>
    <h2 class="person"><span class="person__name">Marcus T. Elbering,</span> <span class="person__title">CPA</span></h2>
    <ul class="contact">
      <li class="contact__item">
        <svg class="contact__icon" viewBox="0 0 22 22" aria-hidden="true">
          <rect x="1.5" y="4.5" width="19" height="13"/>
          <polyline points="1.5,4.5 11,12 20.5,4.5"/>
          <polyline points="1.5,17.5 8.5,10.5"/>
          <polyline points="20.5,17.5 13.5,10.5"/>
        </svg>
        <span>: marcus@fernquill.com</span>
      </li>
      <li class="contact__item">
        <svg class="contact__icon contact__icon--solid" viewBox="0 0 22 22" aria-hidden="true">
          <path d="M2 7 Q11 1 20 7 L18 10 L15 9 L15 7 Q11 5 7 7 L7 9 L4 10 Z"/>
          <path d="M6 11 L16 11 L19 19 L3 19 Z"/>
        </svg>
        <span>: 272-555-0172</span>
      </li>
      <li class="contact__item">
        <svg class="contact__icon contact__icon--solid" viewBox="0 0 22 22" aria-hidden="true">
          <polygon points="11,1 21,6 1,6"/>
          <rect x="3" y="8" width="2.5" height="8"/>
          <rect x="7.5" y="8" width="2.5" height="8"/>
          <rect x="12" y="8" width="2.5" height="8"/>
          <rect x="16.5" y="8" width="2.5" height="8"/>
          <rect x="1" y="17" width="20" height="3"/>
        </svg>
        <span>: 482 N Harlow Ave Halverton,<br>OH 43719</span>
      </li>
    </ul>
  </section>

</main>
</body>
</html>
```